Design the Business card for VaultPeak

Business card required for a professional Cyber Security business.
Company Logo and Icon has already been provided however I would like other options for the logo and icon to compare to. Alternatively, please refine/enhance the image of the logo.icon I have already provided.

If you are going to use the provided logo and icon, I was thinking that the company raised Logo on White background would serve well on the front of the card. See attached. AND, a large company raised stand-alone icon to appear on black background on the back of the card with tagline 'Cyber Risk Management, Governance and Consulting' or 'Cyber Security for your Business' See attached.
Alternatively, provide your own design for the logo and icon.

Target Market(s)

Enterprise, Government, Financial.

Contact Information for Business Card

Teodor Halvik
Founder and CEO

Email Address
Mobile Number
Website URL
LinkedIn URL

Logo Text

VaultPeak - see attached example of logo

Font styles to use
Other font styles liked:
• Berlin Sans FB

Requirements
Must have
• Clean large and bold icon on the back with tagline.
• Horizontal alignment,
Nice to have
• Round edges.
• Raised Logo/Icon
Should not have
• An unprofessional look and feel.

```html
<!DOCTYPE html>
<html lang="en">
<head>
<meta charset="utf-8">
<title>VaultPeak Business Card</title>
<link href="https://fonts.googleapis.com/css2?family=Lato:wght@300;400;700;900&display=swap" rel="stylesheet">
<style>
  :root {
    --stage: #3b3029;
    --card: #050505;
    --brand-blue: #1679d4;
    --icon-blue: #4a72c4;
    --accent-yellow: #f5b90f;
    --text-white: #f2f2f2;
    --text-grey: #bdbdbd;
    --divider: #6a6a6a;
  }
  * { margin: 0; padding: 0; box-sizing: border-box; }
  html, body {
    width: 1200px; height: 715px; overflow: hidden;
    background: var(--stage);
    font-family: "Lato", sans-serif;
  }
  .stage {
    width: 1200px; height: 715px;
    display: flex; align-items: center; justify-content: center; gap: 40px;
  }
  .card {
    position: relative;
    width: 540px; height: 309px;
    background: var(--card);
    border-radius: 8px;
    overflow: hidden;
    box-shadow: 0 14px 30px rgba(0,0,0,0.45);
  }
  .card__band {
    position: absolute; left: 0; right: 0; bottom: 0;
    height: 7px; background: var(--accent-yellow);
  }

  /* Front */
  .front__brand {
    position: absolute; left: 80px; top: 92px;
    display: flex; align-items: center; gap: 18px;
  }
  .brand-dot {
    width: 62px; height: 62px; border-radius: 50%;
    background: var(--icon-blue);
  }
  .brand-name {
    font-weight: 700; font-size: 54px; color: var(--brand-blue);
    letter-spacing: 0.5px;
  }
  .front__tagline {
    position: absolute; left: 92px; top: 212px;
    font-size: 13px; color: var(--text-grey); letter-spacing: 1.6px;
  }

  /* Back */
  .back__mark {
    position: absolute; left: 58px; top: 78px;
    width: 148px; height: 148px; border-radius: 50%;
    background: var(--icon-blue);
  }
  .back__divider {
    position: absolute; left: 252px; top: 72px;
    width: 2px; height: 160px; background: var(--divider);
  }
  .back__details {
    position: absolute; left: 278px; top: 76px;
  }
  .person-name {
    font-size: 20px; color: var(--brand-blue); letter-spacing: 0.3px;
  }
  .person-name__first { font-weight: 300; }
  .person-name__last { font-weight: 700; }
  .person-title {
    font-size: 13px; font-weight: 700; color: var(--text-white);
    margin-top: 2px; margin-bottom: 16px;
  }
  .contact-list { list-style: none; }
  .contact-item {
    display: flex; align-items: center; gap: 10px;
    font-size: 14px; color: var(--text-white);
    margin-bottom: 9px;
  }
  .contact-icon { width: 18px; height: 18px; flex: none; }
  .website {
    margin-top: 10px;
    font-size: 15px; color: var(--brand-blue);
    letter-spacing: 5px; font-weight: 400;
  }
</style>
</head>
<body>
<main class="stage">

  <section class="card card--front" aria-label="Business card front">
    <div class="front__brand">
      <span class="brand-dot"></span>
      <span class="brand-name">VaultPeak</span>
    </div>
    <p class="front__tagline">Cyber Security for your Business</p>
    <div class="card__band"></div>
  </section>

  <section class="card card--back" aria-label="Business card back">
    <div class="back__mark" role="img" aria-label="VaultPeak brand mark"></div>
    <div class="back__divider"></div>
    <div class="back__details">
      <h1 class="person-name">
        <span class="person-name__first">TEODOR</span>
        <span class="person-name__last">HALVIK</span>
      </h1>
      <p class="person-title">Founder and CEO</p>
      <ul class="contact-list">
        <li class="contact-item">
          <svg class="contact-icon" viewBox="0 0 18 18" aria-hidden="true">
            <circle cx="9" cy="9" r="9" fill="#1679d4"/>
            <path d="M6 4.5 L7.6 4.5 L8.3 6.6 L7.3 7.4 Q8.2 9.6 10.6 10.7 L11.4 9.7 L13.5 10.4 L13.5 12 Q12.8 13.3 11 13 Q6.2 11.5 5 7 Q4.8 5.2 6 4.5 Z" fill="#fff"/>
          </svg>
          512.555.0142
        </li>
        <li class="contact-item">
          <svg class="contact-icon" viewBox="0 0 18 18" aria-hidden="true">
            <circle cx="9" cy="9" r="9" fill="#1679d4"/>
            <rect x="4.5" y="5.8" width="9" height="6.4" fill="#fff"/>
            <path d="M4.5 5.8 L9 9.4 L13.5 5.8" fill="none" stroke="#1679d4" stroke-width="1"/>
          </svg>
          teodor@vaultpeak.com
        </li>
        <li class="contact-item">
          <svg class="contact-icon" viewBox="0 0 18 18" aria-hidden="true">
            <circle cx="9" cy="9" r="9" fill="#1679d4"/>
            <circle cx="9" cy="9" r="4.2" fill="none" stroke="#fff" stroke-width="1.2"/>
            <path d="M4.8 9 H13.2 M9 4.8 Q6.6 9 9 13.2 M9 4.8 Q11.4 9 9 13.2" fill="none" stroke="#fff" stroke-width="1"/>
          </svg>
          profiles.vaultpeak.com/teodor
        </li>
      </ul>
      <p class="website">www.vaultpeak.com</p>
    </div>
    <div class="card__band"></div>
  </section>

</main>
</body>
</html>
```